Healthy Lifestyle Vitamin Supplement Company needs a web site designed.

We are starting a new website for selling quality natural vitamins and supplements online plus providing news and information on healthy living. We DO NOT need any programming done for this site. Just the design in a layered photoshop file. This site needs to communicate that we are the authoritative source for healthy living and a trusted place to buy supplements and information on living a healthy lifestyle.

Triggers On page will be

Trigger set 1
Home - Shop By Brand - Top Sellers - Clearance - Help Center - My Favorites

Trigger set 2
Vitamins and Herbs - Natural Living - Aromatherapy - Coffee and Tea - Health and Beauty - Healthy Foods - Pet Health - Sports and Diet

Triggers Other
Login - Shopping Cart - Checkout - Track Order

Need a search bar in the design

Left side should be categories look at Brelvox.com for example of categories.

Name and domain name is Sunward Meadow Crest

Will also need a logo to go along with that.

Industry/Entity Type

It Company

```html
<!DOCTYPE html>
<html lang="en">
<head>
<meta charset="utf-8">
<title>Sunward Meadow Crest – Natural Vitamins & Supplements</title>
<link href="https://fonts.googleapis.com/css2?family=Roboto:wght@300;400;500;700;900&family=Open+Sans:wght@400;600;700&display=swap" rel="stylesheet">
<style>
:root{
  --teal:#22b3a6;
  --teal-dark:#1a958a;
  --orange:#f47b20;
  --ink:#333638;
  --muted:#8a8f93;
  --line:#e3e6e8;
  --soft:#f3f5f6;
  --footer:#2f3234;
  --footer-deep:#262829;
  --white:#ffffff;
  --red:#d9392f;
}
*{box-sizing:border-box;margin:0;padding:0}
html,body{width:1200px;height:2848px;overflow:hidden}
body{position:relative;background:var(--white);font-family:"Open Sans",Arial,sans-serif;color:var(--ink);font-size:12px}
.abs{position:absolute}
h2,h3,h4,.nav a,.btn{font-family:"Roboto",Arial,sans-serif}

/* top bar */
.topbar{left:0;top:0;width:1200px;height:34px;background:var(--ink);color:#c9cdd0;font-size:11px;display:flex;align-items:center;padding:0 100px;justify-content:space-between}
.topbar .contact{display:flex;gap:26px;align-items:center}
.topbar .contact span{display:flex;align-items:center;gap:6px}
.topbar .account{display:flex;gap:22px}

/* header */
.header{left:100px;top:34px;width:1000px;height:86px;display:flex;align-items:center;justify-content:space-between}
.brand{display:flex;align-items:center;gap:10px;font-family:"Roboto",sans-serif;font-weight:700;font-size:25px;color:var(--teal);letter-spacing:-.3px}
.brand .dot{width:26px;height:26px;border-radius:50%;background:var(--teal)}
.nav{display:flex;gap:24px;align-items:center}
.nav a{color:var(--ink);text-decoration:none;font-size:11px;font-weight:700;letter-spacing:.4px}

/* hero */
.greeting{left:100px;top:132px;width:300px;height:356px;background:var(--teal);color:var(--white);text-align:center;padding-top:28px}
.greeting h2{font-size:30px;font-weight:900;letter-spacing:.5px}
.avatar{width:120px;height:120px;border-radius:50%;background:linear-gradient(#ffffff,#e7f4f2);margin:20px auto 18px}
.greeting p{font-size:11px;line-height:16px;padding:0 60px;opacity:.9}
.btn{display:inline-block;font-size:11px;font-weight:700;padding:8px 18px;border-radius:3px;color:var(--white)}
.btn-dark{background:var(--ink);margin-top:16px}
.hero{left:432px;top:132px;width:668px;height:356px;background:var(--soft);overflow:hidden}
.hero h2{position:absolute;left:34px;top:40px;color:var(--red);font-size:36px;font-weight:900;line-height:38px;letter-spacing:.5px}
.hero .lead{position:absolute;left:34px;top:130px;font-family:"Roboto",sans-serif;font-weight:700;font-size:14px;line-height:19px;color:var(--ink)}
.hero .btn-red{position:absolute;left:34px;top:200px;background:var(--red)}
.hero .product-shot{position:absolute;left:300px;top:30px;width:350px;height:310px;background:linear-gradient(180deg,#e9edef,#d7dde0);border-radius:6px}
.badge-sale{position:absolute;left:376px;top:196px;width:108px;height:108px;border-radius:50%;background:var(--orange);color:var(--white);text-align:center;font-family:"Roboto",sans-serif;padding-top:22px}
.badge-sale small{display:block;font-size:13px;font-weight:700}
.badge-sale b{font-size:32px;font-weight:900;line-height:34px}

/* side boxes */
.side-box{left:100px;width:300px;border:1px solid var(--line)}
.side-box h3{background:var(--teal);color:var(--white);font-size:12px;font-weight:700;letter-spacing:.4px;height:34px;line-height:34px;padding-left:14px}
.cat-list{list-style:none;padding:12px 14px}
.cat-list li{display:flex;align-items:center;gap:12px;height:40px;border-bottom:1px solid var(--line);font-size:10px;font-weight:600;text-transform:uppercase;color:#5c6165}
.cat-list li:last-child{border-bottom:0}
.cat-list li i{width:16px;height:16px;border:1px solid var(--teal);border-radius:2px}
.cat-list li.active{color:var(--teal)}
.cat-list li.active i{background:var(--teal)}
.why-item,.blog-item{display:flex;gap:12px;padding:18px 14px}
.why-item .thumb,.blog-item .thumb{flex:0 0 52px;height:52px;background:linear-gradient(#f8c16a,#f29a3c)}
.why-item h4,.blog-item h4{font-size:9px;font-weight:700;color:var(--orange);text-transform:uppercase;margin-bottom:4px}
.why-item p,.blog-item p{font-size:10px;line-height:14px;color:var(--muted)}
.more{font-size:10px;color:var(--teal);font-weight:600;padding:0 14px 14px 78px;display:block}

/* promo */
.promo{left:100px;top:1648px;width:300px;height:672px;background:var(--white);border:1px solid var(--line);overflow:hidden}
.promo .kicker{position:absolute;left:0;width:298px;text-align:center;top:28px;font-size:9px;font-weight:700;color:var(--red);text-transform:uppercase}
.promo .art{position:absolute;left:30px;top:52px;width:240px;height:270px;background:linear-gradient(160deg,#f6b7d1,#a86cc9);border-radius:50% 50% 40% 40%}
.promo .copy{position:absolute;left:34px;top:350px;font-family:"Roboto",sans-serif;color:var(--red)}
.promo .copy small{font-size:14px;font-weight:700;display:block}
.promo .copy b{font-size:54px;font-weight:900;line-height:56px;display:block}
.promo .copy span{font-size:17px;font-weight:700;line-height:22px;color:var(--ink);display:block}
.promo .price{position:absolute;left:150px;top:500px;font-family:"Roboto",sans-serif;color:var(--red);font-size:24px;font-weight:900}
.promo .price small{font-size:11px;display:block}
.promo .ship{position:absolute;left:150px;top:540px;background:var(--red);color:var(--white);font-size:10px;font-weight:700;padding:4px 10px}
.promo .foot{position:absolute;left:0;bottom:0;width:298px;height:66px;background:var(--teal);color:var(--white);display:flex;align-items:center;justify-content:space-between;padding:0 18px;font-family:"Roboto",sans-serif}
.promo .foot b{font-size:18px;font-weight:900}
.promo .foot span{font-size:10px;font-weight:700;text-align:right}

/* product sections */
.section{left:432px;width:668px}
.section-head{display:flex;justify-content:space-between;align-items:center;border-bottom:2px solid var(--teal);height:30px}
.section-head h3{background:var(--teal);color:var(--white);font-size:11px;font-weight:700;letter-spacing:.4px;height:30px;line-height:30px;padding:0 14px}
.arrows{display:flex;gap:4px}
.arrows span{width:22px;height:22px;background:var(--ink);display:flex;align-items:center;justify-content:center}
.view-all{background:var(--ink);color:var(--white);font-size:10px;font-weight:700;padding:5px 10px}
.grid{display:flex;justify-content:space-between;padding-top:18px}
.card{width:150px;position:relative;text-align:center}
.card .shot{height:180px;background:linear-gradient(180deg,#f4f6f5,#e2e8e4);margin-bottom:10px}
.card .tag{position:absolute;left:-4px;top:-6px;width:36px;height:36px;border-radius:50%;background:var(--orange);color:var(--white);font-family:"Roboto",sans-serif;font-size:11px;font-weight:700;line-height:36px}
.stars{color:var(--orange);font-size:10px;letter-spacing:1px}
.card h4{font-size:11px;font-weight:700;margin:4px 0 3px}
.card p{font-size:9px;line-height:12px;color:var(--muted);padding:0 6px}
.card .price{color:var(--red);font-family:"Roboto",sans-serif;font-weight:700;font-size:13px;margin:6px 0}
.card .actions{display:flex;justify-content:center;gap:4px}
.card .actions .add{background:#9aa0a4;color:var(--white);font-size:9px;font-weight:700;padding:4px 10px}
.card .actions .fav{background:var(--teal);width:22px;display:flex;align-items:center;justify-content:center}

.brands{display:flex;justify-content:space-around;align-items:center;height:80px;border:1px solid var(--line);border-top:0}
.brands span{font-family:"Roboto",sans-serif;font-weight:700;font-size:20px;color:#55595c}

/* quote band */
.quote{left:0;top:2420px;width:1200px;height:62px;background:var(--soft);display:flex;align-items:center;justify-content:center;gap:12px;font-size:12px;font-style:italic;color:#5c6165}

/* footer */
.footer{left:0;top:2496px;width:1200px;height:222px;background:var(--footer);color:#aeb3b6;padding:32px 100px 0;display:flex;gap:40px}
.footer .col{width:150px}
.footer h4{color:var(--white);font-size:10px;font-weight:700;margin-bottom:12px;text-transform:uppercase}
.footer li{list-style:none;font-size:9px;line-height:15px}
.footer .read{color:var(--white);font-size:9px;margin-top:10px;display:block}
.footer .signup{width:230px}
.footer .signup .field{display:flex;height:26px;margin-bottom:10px}
.footer .signup .field span{flex:1;background:var(--white);color:#999;font-size:9px;line-height:26px;padding-left:8px}
.footer .signup .field b{width:50px;background:var(--teal);color:var(--white);font-size:9px;text-align:center;line-height:26px}
.footer .signup p{font-size:9px;line-height:14px}
.subfoot{left:0;top:2718px;width:1200px;height:44px;background:var(--footer-deep);display:flex;align-items:center;justify-content:space-between;padding:0 100px;color:#d0d3d5;font-size:10px}
.subfoot .sel{display:flex;gap:10px}
.subfoot .sel span{border:1px solid #4a4e51;padding:4px 10px}
.socials{display:flex;gap:6px}
.socials i{width:22px;height:22px;border-radius:2px;background:var(--teal)}
.legal{left:0;top:2772px;width:1200px;text-align:center;font-size:9px;line-height:14px;color:var(--muted)}
.legal a{color:var(--teal)}
.payments{left:0;top:2808px;width:1200px;display:flex;justify-content:center;gap:12px}
.payments i{width:54px;height:24px;border:1px solid var(--line);background:var(--soft);border-radius:3px}
.payments i.seal{width:40px;background:#e0e4e6;border:0}
</style>
</head>
<body>

<div class="abs topbar">
  <span>Alex Rowan, welcome to our online store!</span>
  <div class="contact">
    <span><svg width="10" height="10" viewBox="0 0 10 10"><path d="M2 0h2l1 3-1.5 1a6 6 0 0 0 2.5 2.5L7 5l3 1v2c0 1-1 2-2 2A8 8 0 0 1 0 2c0-1 1-2 2-2z" fill="#22b3a6"/></svg>(800) 555 0142</span>
    <span><svg width="11" height="8" viewBox="0 0 11 8"><rect x=".5" y=".5" width="10" height="7" fill="none" stroke="#22b3a6"/><path d="M.5.5l5 4 5-4" fill="none" stroke="#22b3a6"/></svg>hello@brelvox.com</span>
  </div>
  <div class="account"><span>Login</span><span>My Account ▾</span><span>Cart: 0 item</span><span>Checkout</span></div>
</div>

<header class="abs header">
  <div class="brand"><span class="dot"></span>Sunward Meadow Crest</div>
  <nav class="nav">
    <a>HOME</a><a>SHOP BY BRAND</a><a>TOP SELLERS</a><a>CLEARANCE</a><a>HELP CENTER</a><a>MY FAVORITES</a>
    <svg width="14" height="14" viewBox="0 0 14 14"><circle cx="6" cy="6" r="4.5" fill="none" stroke="#333638" stroke-width="2"/><path d="M9.5 9.5l3.5 3.5" stroke="#333638" stroke-width="2"/></svg>
  </nav>
</header>

<section class="abs greeting">
  <h2>HI ALEX ROWAN!</h2>
  <div class="avatar" role="img" aria-label="Cartoon member avatar"></div>
  <p>Your account and saved lists are ready. See what is new this week.</p>
  <span class="btn btn-dark">Learn more</span>
</section>

<section class="abs hero">
  <h2>ACCUSANTI<br>LAUDANTIUM</h2>
  <div class="lead">PERSPICIATIS DOLORE<br>TOTAM UNDE UNDE ET<br>AUT ILLO AUT</div>
  <span class="btn btn-red">pre-order now</span>
  <div class="product-shot" role="img" aria-label="Vireltha protein tubs and supplement boxes"></div>
  <div class="badge-sale"><small>up to</small><b>50%</b><small>OFF</small></div>
</section>

<aside class="abs side-box" style="top:520px;height:380px">
  <h3>SHOP BY CATEGORY</h3>
  <ul class="cat-list">
    <li class="active"><i></i>Vitamins and Herbs</li>
    <li><i></i>Natural Living</li>
    <li><i></i>Aromatherapy</li>
    <li><i></i>Coffee and Tea</li>
    <li><i></i>Health and Beauty</li>
    <li><i></i>Healthy Foods</li>
    <li><i></i>Pet Health</li>
    <li><i></i>Sports and Diet</li>
  </ul>
</aside>

<aside class="abs side-box" style="top:928px;height:392px">
  <h3>WHY YOU CHOOSE US</h3>
  <div class="why-item"><div class="thumb" role="img" aria-label="Quality seal photo"></div><div><h4>Tested Quality</h4><p>Every batch is checked by an outside lab before it reaches our shelf.</p></div></div>
  <div class="why-item"><div class="thumb" role="img" aria-label="Shipping box photo"></div><div><h4>Fast Shipping</h4><p>Orders leave our warehouse within one working day, tracked to your door.</p></div></div>
  <div class="why-item"><div class="thumb" role="img" aria-label="Customer support photo"></div><div><h4>Friendly Experts</h4><p>Our wellness team answers your questions by phone, chat or email.</p></div></div>
</aside>

<aside class="abs side-box" style="top:1352px;height:280px">
  <h3>NEWS FROM BLOG</h3>
  <div class="blog-item"><div class="thumb" role="img" aria-label="Blog article photo"></div><div><h4>Morning Habits</h4><p>Five small changes that help you start each day with more energy.</p></div></div>
  <span class="more">Read more ›</span>
  <div class="blog-item" style="padding-top:4px"><div class="thumb" role="img" aria-label="Blog article photo"></div><div><h4>Eat The Rainbow</h4><p>Why colourful plates bring a wider range of nutrients to your diet.</p></div></div>
</aside>

<aside class="abs promo">
  <span class="kicker">Special offer</span>
  <div class="art" role="img" aria-label="Cartoon dinosaur holding gummy vitamins"></div>
  <div class="copy"><small>ENJOY OVER</small><b>50% OFF</b><span>Pure Fibrelle<br>Multivitamin<br>Gummies</span></div>
  <div class="price"><small>JUST</small>$9.95</div>
  <span class="ship">FREE SHIPPING</span>
  <div class="foot"><b>Pure Fibrelle</b><span>GET IT NOW<br>WHILE STOCK LASTS</span></div>
</aside>

<section class="abs section" style="top:520px">
  <div class="section-head"><h3>NEW PRODUCTS OF THE WEEK</h3><div class="arrows"><span><svg width="6" height="8"><path d="M5 0L1 4l4 4" stroke="#fff" fill="none"/></svg></span><span><svg width="6" height="8"><path d="M1 0l4 4-4 4" stroke="#fff" fill="none"/></svg></span></div></div>
  <div class="grid">
    <div class="card"><span class="tag">NEW</span><div class="shot" role="img" aria-label="Supplement bottle"></div><div class="stars">★★★★★</div><h4>Vitamin D3 2000</h4><p>Daily support for bones and a healthy immune system</p><div class="price">$ 123.00</div><div class="actions"><span class="add">add</span><span class="fav"><svg width="10" height="9" viewBox="0 0 10 9"><path d="M5 9L1 5a2.4 2.4 0 0 1 4-3 2.4 2.4 0 0 1 4 3z" fill="#fff"/></svg></span></div></div>
    <div class="card"><div class="shot" role="img" aria-label="Supplement bottle"></div><div class="stars">★★★★★</div><h4>Herbal Green Blend</h4><p>A balanced mix of leafy herbs for daily wellness</p><div class="price">$ 123.00</div><div class="actions"><span class="add">add</span><span class="fav"><svg width="10" height="9" viewBox="0 0 10 9"><path d="M5 9L1 5a2.4 2.4 0 0 1 4-3 2.4 2.4 0 0 1 4 3z" fill="#fff"/></svg></span></div></div>
    <div class="card"><span class="tag">NEW</span><div class="shot" role="img" aria-label="Supplement bottle"></div><div class="stars">★★★★★</div><h4>Omega Fish Oil</h4><p>Pure softgels for heart, brain and joint comfort</p><div class="price">$ 123.00</div><div class="actions"><span class="add">add</span><span class="fav"><svg width="10" height="9" viewBox="0 0 10 9"><path d="M5 9L1 5a2.4 2.4 0 0 1 4-3 2.4 2.4 0 0 1 4 3z" fill="#fff"/></svg></span></div></div>
    <div class="card"><div class="shot" role="img" aria-label="Supplement bottle"></div><div class="stars">★★★★★</div><h4>Calcium Magnesium</h4><p>Mineral pair that keeps muscles and bones strong</p><div class="price">$ 123.00</div><div class="actions"><span class="add">add</span><span class="fav"><svg width="10" height="9" viewBox="0 0 10 9"><path d="M5 9L1 5a2.4 2.4 0 0 1 4-3 2.4 2.4 0 0 1 4 3z" fill="#fff"/></svg></span></div></div>
  </div>
</section>

<section class="abs section" style="top:928px">
  <div class="section-head"><h3>BESTSELLER PRODUCTS</h3><div class="arrows"><span><svg width="6" height="8"><path d="M5 0L1 4l4 4" stroke="#fff" fill="none"/></svg></span><span><svg width="6" height="8"><path d="M1 0l4 4-4 4" stroke="#fff" fill="none"/></svg></span></div></div>
  <div class="grid">
    <div class="card"><div class="shot" role="img" aria-label="Supplement bottle"></div><div class="stars">★★★★★</div><h4>Probiotic 10 Billion</h4><p>Friendly cultures for smooth and easy digestion</p><div class="price">$ 123.00</div><div class="actions"><span class="add">add</span><span class="fav"><svg width="10" height="9" viewBox="0 0 10 9"><path d="M5 9L1 5a2.4 2.4 0 0 1 4-3 2.4 2.4 0 0 1 4 3z" fill="#fff"/></svg></span></div></div>
    <div class="card"><span class="tag">5%</span><div class="shot" role="img" aria-label="Supplement bottle"></div><div class="stars">★★★★★</div><h4>Vitamin C 1000</h4><p>Antioxidant tablets with rose hips for daily use</p><div class="price">$ 123.00</div><div class="actions"><span class="add">add</span><span class="fav"><svg width="10" height="9" viewBox="0 0 10 9"><path d="M5 9L1 5a2.4 2.4 0 0 1 4-3 2.4 2.4 0 0 1 4 3z" fill="#fff"/></svg></span></div></div>
    <div class="card"><span class="tag">2%</span><div class="shot" role="img" aria-label="Supplement bottle"></div><div class="stars">★★★★★</div><h4>Turmeric Curcumin</h4><p>Golden root extract with black pepper for comfort</p><div class="price">$ 123.00</div><div class="actions"><span class="add">add</span><span class="fav"><svg width="10" height="9" viewBox="0 0 10 9"><path d="M5 9L1 5a2.4 2.4 0 0 1 4-3 2.4 2.4 0 0 1 4 3z" fill="#fff"/></svg></span></div></div>
    <div class="card"><div class="shot" role="img" aria-label="Supplement bottle"></div><div class="stars">★★★★★</div><h4>Zinc Picolinate</h4><p>Easy absorbing mineral for skin and immune health</p><div class="price">$ 123.00</div><div class="actions"><span class="add">add</span><span class="fav"><svg width="10" height="9" viewBox="0 0 10 9"><path d="M5 9L1 5a2.4 2.4 0 0 1 4-3 2.4 2.4 0 0 1 4 3z" fill="#fff"/></svg></span></div></div>
  </div>
</section>

<section class="abs section" style="top:1352px">
  <div class="section-head"><h3>FEATURED PRODUCTS</h3><span class="view-all">view all</span></div>
  <div class="grid">
    <div class="card"><div class="shot" role="img" aria-label="Supplement bottle"></div><div class="stars">★★★★★</div><h4>B Complex 100</h4><p>Full family of B vitamins for steady daily energy</p><div class="price">$ 123.00</div><div class="actions"><span class="add">add</span><span class="fav"><svg width="10" height="9" viewBox="0 0 10 9"><path d="M5 9L1 5a2.4 2.4 0 0 1 4-3 2.4 2.4 0 0 1 4 3z" fill="#fff"/></svg></span></div></div>
    <div class="card"><div class="shot" role="img" aria-label="Supplement bottle"></div><div class="stars">★★★★★</div><h4>Milk Thistle</h4><p>Classic herbal extract that supports liver health</p><div class="price">$ 123.00</div><div class="actions"><span class="add">add</span><span class="fav"><svg width="10" height="9" viewBox="0 0 10 9"><path d="M5 9L1 5a2.4 2.4 0 0 1 4-3 2.4 2.4 0 0 1 4 3z" fill="#fff"/></svg></span></div></div>
    <div class="card"><div class="shot" role="img" aria-label="Supplement bottle"></div><div class="stars">★★★★★</div><h4>Iron Gentle</h4><p>Soft on the stomach formula with added vitamin C</p><div class="price">$ 123.00</div><div class="actions"><span class="add">add</span><span class="fav"><svg width="10" height="9" viewBox="0 0 10 9"><path d="M5 9L1 5a2.4 2.4 0 0 1 4-3 2.4 2.4 0 0 1 4 3z" fill="#fff"/></svg></span></div></div>
    <div class="card"><div class="shot" role="img" aria-label="Supplement bottle"></div><div class="stars">★★★★★</div><h4>Melatonin 3mg</h4><p>Quick dissolve tablets for calm and restful sleep</p><div class="price">$ 123.00</div><div class="actions"><span class="add">add</span><span class="fav"><svg width="10" height="9" viewBox="0 0 10 9"><path d="M5 9L1 5a2.4 2.4 0 0 1 4-3 2.4 2.4 0 0 1 4 3z" fill="#fff"/></svg></span></div></div>
  </div>
  <div class="grid" style="padding-top:60px">
    <div class="card"><div class="shot" role="img" aria-label="Supplement bottle"></div><div class="stars">★★★★★</div><h4>Biotin 5000</h4><p>Beauty vitamin for healthy hair, skin and nails</p><div class="price">$ 123.00</div><div class="actions"><span class="add">add</span><span class="fav"><svg width="10" height="9" viewBox="0 0 10 9"><path d="M5 9L1 5a2.4 2.4 0 0 1 4-3 2.4 2.4 0 0 1 4 3z" fill="#fff"/></svg></span></div></div>
    <div class="card"><div class="shot" role="img" aria-label="Supplement bottle"></div><div class="stars">★★★★★</div><h4>Echinacea Root</h4><p>Seasonal herbal support when the weather turns</p><div class="price">$ 123.00</div><div class="actions"><span class="add">add</span><span class="fav"><svg width="10" height="9" viewBox="0 0 10 9"><path d="M5 9L1 5a2.4 2.4 0 0 1 4-3 2.4 2.4 0 0 1 4 3z" fill="#fff"/></svg></span></div></div>
    <div class="card"><div class="shot" role="img" aria-label="Supplement bottle"></div><div class="stars">★★★★★</div><h4>CoQ10 100mg</h4><p>Cellular energy support for an active lifestyle</p><div class="price">$ 123.00</div><div class="actions"><span class="add">add</span><span class="fav"><svg width="10" height="9" viewBox="0 0 10 9"><path d="M5 9L1 5a2.4 2.4 0 0 1 4-3 2.4 2.4 0 0 1 4 3z" fill="#fff"/></svg></span></div></div>
    <div class="card"><div class="shot" role="img" aria-label="Supplement bottle"></div><div class="stars">★★★★★</div><h4>Glucosamine Plus</h4><p>Joint formula with chondroitin for easy movement</p><div class="price">$ 123.00</div><div class="actions"><span class="add">add</span><span class="fav"><svg width="10" height="9" viewBox="0 0 10 9"><path d="M5 9L1 5a2.4 2.4 0 0 1 4-3 2.4 2.4 0 0 1 4 3z" fill="#fff"/></svg></span></div></div>
  </div>
</section>

<section class="abs section" style="top:2328px">
  <div class="section-head"><h3>SEARCH BY BRAND</h3></div>
  <div class="brands"><span>Nurvello</span><span>Azmeron</span><span>Cavindor</span><span>Sorvanta</span><span>Pixelmond</span></div>
</section>

<div class="abs quote">
  <svg width="16" height="13" viewBox="0 0 16 13"><path d="M1 7l4 4 10-10" fill="none" stroke="#22b3a6" stroke-width="2.4"/></svg>
  “I have never had a shop so patient in explaining every label to me.” – Martin Ellery
</div>

<footer class="abs footer">
  <div class="col"><h4>Who we are</h4><ul><li>Our story and values</li><li>Meet the wellness team</li><li>Quality promise</li><li>Careers</li></ul><span class="read">Read more ›</span></div>
  <div class="col"><h4>What we sell</h4><ul><li>Vitamins and herbs</li><li>Natural living</li><li>Healthy foods</li><li>Sports and diet</li></ul><span class="read">Read more ›</span></div>
  <div class="col"><h4>Shipping</h4><ul><li>Delivery options</li><li>Free shipping rules</li><li>Returns policy</li><li>International orders</li></ul><span class="read">Read more ›</span></div>
  <div class="col"><h4>Track your order</h4><ul><li>Order status</li><li>Shopping cart</li><li>Checkout help</li><li>Contact support</li></ul><span class="read">Read more ›</span></div>
  <div class="signup"><h4>Sign up for special deals</h4><div class="field"><span>Your email address</span><b>JOIN</b></div><p>Weekly offers and healthy living tips sent straight to your inbox.</p></div>
</footer>

<div class="abs subfoot">
  <div class="sel"><span>United States – English ▾</span><span>Currency US$ ▾</span></div>
  <div class="socials"><i></i><i></i><i></i><i></i><i></i></div>
</div>

<div class="abs legal">
  Use of this site is subject to our <a>terms of use</a>. By using this site, you agree to be bound by them.<br>
  <a>Terms of Service</a> · <a>Privacy Policy</a> · © 2024 Sunward Meadow Crest. All Rights Reserved.
</div>
<div class="abs payments"><i class="seal"></i><i class="seal"></i><i class="seal"></i><i></i><i></i><i></i><i></i><i></i><i></i></div>

</body>
</html>
```